Memoir author looking for book cover design

Title:
"Rain, Rust and Return"

Subtitle:
"A Season Spent Chasing Our Father Across the Coastline"

My book is about the 18-month-long search and grieving process after my husband went missing from a hiking accident.
See "notesbeyondthequietharbor.example" for background

(An "ampersand" may look best, but I'm unable to enter it in this format)

Reason: Having difficulty finishing up, in part due to time difference. Don't want designers to have to work in the middle of the night!

```html
<!DOCTYPE html>
<html lang="en">
<head>
<meta charset="utf-8">
<title>Rain, Rust and Return — Cover</title>
<link rel="stylesheet" href="https://fonts.googleapis.com/css2?family=Aleo:wght@400;500&display=swap">
<style>
  :root {
    --page-bg: #efe9df;
    --sky-top: #aab6cf;
    --sky-mid: #b3b8d0;
    --ridge-light: #5a7cc0;
    --ridge-blue: #3f5fa8;
    --ridge-deep: #2b3b7a;
    --valley-navy: #1e2150;
    --hair-light: #e2bf9a;
    --hair-mid: #d4ab84;
    --hair-deep: #c59a74;
    --title-red: #e2141c;
    --ink: #0b0b0b;
    --label-white: #ffffff;
  }
  * { box-sizing: border-box; margin: 0; padding: 0; }
  html, body {
    width: 1200px;
    height: 1200px;
    overflow: hidden;
    background: var(--page-bg);
  }
  .canvas {
    position: relative;
    width: 1200px;
    height: 1200px;
  }
  .cover {
    position: absolute;
    left: 225px;
    top: 40px;
    width: 750px;
    height: 1120px;
    overflow: hidden;
    box-shadow: 0 18px 40px rgba(0, 0, 0, 0.18);
    font-family: "Aleo", Georgia, serif;
  }
  .cover-landscape {
    position: absolute;
    inset: 0;
    background: linear-gradient(
      180deg,
      var(--sky-top) 0%,
      var(--sky-mid) 30%,
      var(--ridge-light) 38%,
      var(--ridge-blue) 50%,
      var(--ridge-deep) 62%,
      var(--valley-navy) 70%,
      var(--valley-navy) 100%
    );
  }
  .cover-figure {
    position: absolute;
    left: 215px;
    top: 500px;
    right: 0;
    bottom: 0;
    border-radius: 240px 260px 0 0;
    background: linear-gradient(
      160deg,
      var(--hair-light) 0%,
      var(--hair-mid) 55%,
      var(--hair-deep) 100%
    );
  }
  .title-word {
    position: absolute;
    line-height: 1;
    font-weight: 400;
    text-transform: uppercase;
    color: var(--ink);
  }
  .title-word--boxed {
    background: var(--label-white);
    padding: 4px 14px 0 10px;
  }
  .title-word--rain {
    left: 40px;
    top: 20px;
    font-size: 150px;
    color: var(--title-red);
  }
  .title-word--rust {
    left: 175px;
    top: 148px;
    font-size: 150px;
  }
  .title-ampersand {
    left: 70px;
    top: 262px;
    font-size: 112px;
  }
  .title-word--return {
    left: 92px;
    top: 350px;
    font-size: 118px;
  }
  .strike-line {
    position: absolute;
    left: 88px;
    top: 408px;
    width: 582px;
    height: 4px;
    background: var(--ink);
  }
  .subtitle {
    position: absolute;
    left: 18px;
    top: 612px;
    font-size: 31px;
    line-height: 1.05;
    color: var(--ink);
  }
  .subtitle-line {
    display: table;
    background: var(--label-white);
    padding: 0 8px 2px 6px;
  }
  .subtitle-line + .subtitle-line {
    margin-left: 42px;
  }
  .author-name {
    position: absolute;
    right: 14px;
    bottom: 28px;
    font-size: 50px;
    letter-spacing: 0.5px;
    color: var(--ink);
    text-transform: uppercase;
  }
</style>
</head>
<body>
  <main class="canvas">
    <section class="cover">
      <div class="cover-landscape" role="img" aria-label="Illustration: layered blue mountain ranges under a pale sky with pink cloud streaks"></div>
      <div class="cover-figure" role="img" aria-label="Illustration: a long-haired woman seen from behind, gazing out over the mountain valley"></div>

      <h1 class="title" aria-label="Rain, Rust and Return">
        <span class="title-word title-word--boxed title-word--rain">Rain</span>
        <span class="title-word title-word--boxed title-word--rust">Rust</span>
        <span class="title-word title-ampersand">&amp;</span>
        <span class="title-word title-word--return">Return</span>
        <span class="strike-line"></span>
      </h1>

      <p class="subtitle">
        <span class="subtitle-line">A Season Spent Chasing Our Father</span>
        <span class="subtitle-line">Across the Coastline</span>
      </p>

      <p class="author-name">Author Name</p>
    </section>
  </main>
</body>
</html>
```